Business Card Design for Oncology Consulting Company

We need a business card design using a logo that has already been created.

Company name is: WMBHO - Guild for Tumor Projection, Therapy and Remediation

We would also like to include the following pieces of information on the business card:
Name
Title
US Address (street, city, state, zip, country)
Email address
Website address

Target Market(s)

The target customers are physicians (oncologists, pathologists) in Greece, Iran, US, etc who would refer patients to our company for a second medical opinion/genetic counseling for cancer.

Industry/Entity Type

Business

Colors

Designer to choose colors to be used in the design.

Requirements
Must have
• Must contain logo in attached file and elements described above.

```html
<!DOCTYPE html>
<html lang="en">
<head>
<meta charset="utf-8">
<title>WMBHO Business Card</title>
<link rel="stylesheet" href="https://fonts.googleapis.com/css2?family=Ubuntu:wght@400;500;700&display=swap">
<style>
  :root {
    --brand-blue: #0067ad;
    --band-light: #2f83bf;
    --paper: #ffffff;
    --rule-grey: #bfbfbf;
    --tag-grey: #9a9a9a;
    --backdrop: #d5d6d8;
  }
  * { margin: 0; padding: 0; box-sizing: border-box; }
  html, body { width: 1200px; height: 1000px; overflow: hidden; }
  body {
    position: relative;
    background: var(--backdrop);
    font-family: "Ubuntu", sans-serif;
  }
  .card {
    position: absolute;
    overflow: hidden;
  }

  /* Front */
  .card-front {
    left: 75px; top: 60px;
    width: 740px; height: 423px;
    background: var(--brand-blue);
    color: var(--paper);
  }
  .front-name {
    position: absolute;
    top: 62px; left: 0; right: 0;
    text-align: center;
    font-size: 88px;
    font-weight: 500;
    line-height: 1;
  }
  .front-band {
    position: absolute;
    left: 0; right: 0;
    top: 185px; height: 120px;
    background: linear-gradient(90deg, var(--brand-blue), var(--band-light) 50%, var(--brand-blue));
  }
  .front-rule {
    position: absolute;
    left: 30px; right: 0;
    top: 318px; height: 6px;
    background: var(--paper);
  }
  .front-tagline {
    position: absolute;
    left: 30px; right: 0;
    top: 345px;
    text-align: center;
    font-size: 17px;
    font-weight: 700;
    letter-spacing: 0.3px;
    text-transform: uppercase;
    white-space: nowrap;
  }

  /* Back */
  .card-back {
    left: 400px; top: 500px;
    width: 760px; height: 434px;
    background: var(--brand-blue);
    color: var(--paper);
  }
  .back-header {
    position: absolute;
    left: 0; top: 0; right: 0;
    height: 225px;
    background: var(--paper);
  }
  .back-name {
    position: absolute;
    left: 36px; top: 96px;
    font-size: 76px;
    font-weight: 500;
    color: var(--brand-blue);
    line-height: 1;
    white-space: nowrap;
  }
  .back-rule {
    position: absolute;
    left: 362px; width: 350px;
    top: 118px; height: 4px;
    background: var(--rule-grey);
  }
  .back-tagline {
    position: absolute;
    left: 362px; width: 350px;
    top: 126px;
    font-size: 9.5px;
    font-weight: 700;
    color: var(--tag-grey);
    text-transform: uppercase;
    letter-spacing: 0.2px;
    white-space: nowrap;
  }
  .person {
    position: absolute;
    left: 55px; top: 280px;
  }
  .person-name {
    font-size: 23px;
    font-weight: 500;
    letter-spacing: 2.5px;
    text-transform: uppercase;
  }
  .person-title {
    font-size: 19px;
    font-weight: 400;
  }
  .contact {
    position: absolute;
    left: 445px; top: 250px;
    font-size: 22px;
    line-height: 1.4;
    list-style: none;
    white-space: nowrap;
  }
  .address {
    position: absolute;
    left: 0; right: 0;
    top: 360px;
    text-align: center;
    font-size: 22px;
  }
</style>
</head>
<body>

  <section class="card card-front">
    <div class="front-name">WMBHO</div>
    <div class="front-band" role="img" aria-label="Decorative band in the brand blue tones"></div>
    <div class="front-rule"></div>
    <div class="front-tagline">Guild for Tumor Projection, Therapy and Remediation</div>
  </section>

  <section class="card card-back">
    <header class="back-header">
      <div class="back-name">WMBHO</div>
      <div class="back-rule"></div>
      <div class="back-tagline">Guild for Tumor Projection, Therapy and Remediation</div>
    </header>
    <div class="person">
      <div class="person-name">Dana K.</div>
      <div class="person-title">General Manager</div>
    </div>
    <ul class="contact">
      <li>(E): dana@wmbho.com</li>
      <li>(W): www.wmbho.com</li>
    </ul>
    <div class="address">240, Harbor Street, Portland, OR 97204</div>
  </section>

</body>
</html>
```